Biz card for my counselling/social work practice

Biz card design for my counselling practice, focus on well-being, I am a social worker who also teaches meditation and workshops but my main focus for the card is my counselling practice. My website reveals a gentle flowing quality which I would life reflected in my card. This business card will be designed to share with other practitioners who are looking for support with their clients to take their healing to another level or well-being.

Target Market(s)

professionals seeking mental health counselling/men/women/ those seeking to improve their well-being through insight based counselling to optimize their lives and process trauma or limiting patterns

Industry/Entity Type

Counsellor

Contact Information for Business Card

Info on the card: perhaps text is aligned left?
Maribel Strand, MSW, RSW
Counsellor
614.295.3140
info@maribelstrand.example
www.maribelstrand.example

Please use a modern font doesn’t need to be the one chosen below. Thank you

Font styles to use
Serif

Colors
3176b5
33a6d7
33b8a4
6b449b
abd037
d2a4cc
e55fa2

Requirements
Must have
• My business card details on front
• Backside
• Accelerated Resolution Therapy
• Cognitive Behavioral Therapy
• Mindfulness Informed Therapy
Nice to have
• I would like the card to be basic, (white or creme without too much bold colour) and with perhaps a stripe or band of vertical colour in blue or green (or a merge of colour) perhaps embossed or in a negative space. (this is one idea, but do not want the card to be too feminine or interest only women as i see men too so this is only an idea, but not 100 percent on this.
• I do not have a logo. I would prefer to heart from my website not to be used in the design as i am considering modifying this and re-branding.
Should not have
• too bold colours or bright yellow/blacks. i Like tones that are greens, blues.

```html
<!DOCTYPE html>
<html lang="en">
<head>
<meta charset="utf-8">
<title>Maribel Strand — Business Card</title>
<link href="https://fonts.googleapis.com/css2?family=Montserrat:wght@400;500;700&display=swap" rel="stylesheet">
<style>
  :root {
    --page-bg: #ffffff;
    --card-bg: #ffffff;
    --ink: #111111;
    --ink-soft: #2b2b2b;
    --accent: #2f6a84;
    --shadow: rgba(0, 0, 0, 0.10);
  }
  * { margin: 0; padding: 0; box-sizing: border-box; }
  html, body {
    width: 1200px;
    height: 1200px;
    overflow: hidden;
    background: var(--page-bg);
  }
  .stage {
    position: relative;
    width: 1200px;
    height: 1200px;
  }
  .card {
    position: absolute;
    left: 222px;
    width: 758px;
    height: 424px;
    background: var(--card-bg);
    box-shadow: 0 12px 40px var(--shadow);
    overflow: hidden;
  }
  .card--front { top: 128px; }
  .card--back  { top: 646px; }

  .identity {
    position: absolute;
    left: 54px;
    top: 66px;
    font-family: "Montserrat", sans-serif;
    font-weight: 700;
    font-size: 20px;
    letter-spacing: 3.6px;
    color: var(--ink);
    line-height: 45px;
  }
  .identity__role {
    display: block;
    margin-top: -6px;
    font-weight: 500;
    font-size: 15px;
    letter-spacing: 3px;
    line-height: 24px;
    color: var(--accent);
  }
  .contact {
    position: absolute;
    left: 54px;
    top: 204px;
    list-style: none;
    font-family: "Montserrat", sans-serif;
    font-weight: 400;
    font-size: 20px;
    letter-spacing: 2.6px;
    color: var(--ink);
    line-height: 37px;
  }
  .accent-stripe {
    position: absolute;
    left: 590px;
    top: 0;
    width: 6px;
    height: 318px;
    background: var(--accent);
  }
  .wordmark {
    position: absolute;
    right: 28px;
    top: 356px;
    display: flex;
    align-items: center;
    gap: 10px;
    font-family: "Montserrat", sans-serif;
    font-weight: 400;
    font-size: 26px;
    letter-spacing: 0.5px;
    color: var(--accent);
  }
  .wordmark__dot {
    width: 12px;
    height: 12px;
    border-radius: 50%;
    background: var(--accent);
  }
  .portrait-area {
    position: absolute;
    inset: 0;
    background:
      radial-gradient(ellipse 30% 60% at 78% 55%, #b08a6c 0%, rgba(176,138,108,0) 70%),
      linear-gradient(100deg, #c7cfd6 0%, #b9c1bf 26%, #8e9870 44%, #4f5f3a 62%, #5a5238 80%, #2d2a26 100%);
  }
  .services {
    position: absolute;
    left: 44px;
    top: 48px;
    list-style: none;
    font-family: "Montserrat", sans-serif;
    font-weight: 500;
    font-size: 15px;
    letter-spacing: 1.6px;
    line-height: 32px;
    color: var(--ink-soft);
  }
</style>
</head>
<body>
  <main class="stage">
    <section class="card card--front" aria-label="Card front">
      <h1 class="identity">
        <span class="identity__name">MARIBEL STRAND</span><br>
        <span class="identity__credentials">MSW, RSW</span>
        <span class="identity__role">COUNSELLOR</span>
      </h1>
      <ul class="contact">
        <li class="contact__phone">614.295.3140</li>
        <li class="contact__email">info@maribelstrand.example</li>
        <li class="contact__web">www.maribelstrand.example</li>
      </ul>
      <div class="accent-stripe"></div>
      <div class="wordmark">
        <span class="wordmark__name">Maribel Strand</span>
        <span class="wordmark__dot"></span>
      </div>
    </section>

    <section class="card card--back" aria-label="Card back">
      <div class="portrait-area" role="img" aria-label="Outdoor portrait photograph of the counsellor smiling, with soft-focus trees, grasses and pale sky behind"></div>
      <ul class="services">
        <li>Accelerated Resolution Therapy</li>
        <li>Cognitive Behavioral Therapy</li>
        <li>Mindfulness Informed Therapy</li>
      </ul>
    </section>
  </main>
</body>
</html>
```